The Velmira Circle

I need a design for a 1 page flyer but also a brochure

Target Market(s)

Wealthy, elegant, intelligent, discerning women who are on a journey of self-discovery.

Industry/Entity Type

Spiritual and personal development, yoga, meditation

Requirements
Must have
• Be very elegant, attractive, upmarket minimalist but also bit mystical
Nice to have
• I would like to use my logo (see uploaded file). The texts are also uploaded. One for the 1 page flyer 1 for a full brochure
Should not have
• be too busy, multicoloured, garish.

```html
<!DOCTYPE html>
<html lang="en">
<head>
<meta charset="utf-8">
<title>The Velmira Circle – Retreat Brochure</title>
<link rel="stylesheet" href="https://fonts.googleapis.com/css2?family=Poppins:wght@300;400;500;600;700&family=Marcellus&family=Playfair+Display:wght@600&display=swap">
<style>
  :root {
    --backdrop: #a4a4a4;
    --forest: #0b4a25;
    --forest-deep: #093f1f;
    --leaf: #1fc83c;
    --heading: #0e5a2a;
    --ink: #1d1d1d;
    --mist-1: #f3f8f0;
    --mist-2: #dcebd6;
    --mist-3: #c9e0c2;
    --logo-grey: #8c8c8c;
    --white: #ffffff;
  }
  * { margin: 0; padding: 0; box-sizing: border-box; }
  html, body { width: 770px; height: 1200px; overflow: hidden; }
  body { background: var(--backdrop); font-family: "Poppins", sans-serif; color: var(--ink); position: relative; }

  .spread {
    position: absolute; left: 57px; width: 656px; height: 507px; overflow: hidden;
    background:
      radial-gradient(ellipse at 30% 20%, var(--mist-1) 0%, transparent 60%),
      radial-gradient(ellipse at 80% 85%, var(--mist-3) 0%, transparent 55%),
      linear-gradient(160deg, var(--mist-1) 0%, var(--mist-2) 55%, var(--mist-3) 100%);
  }
  .spread--outside { top: 71px; }
  .spread--inside { top: 624px; }
  .abs { position: absolute; }

  .photo { position: absolute; }
  .photo--kneeling { left: 2px; top: 39px; width: 168px; height: 185px; border-radius: 6px;
    background: linear-gradient(180deg, #e7ece6 0%, #c9cdc8 55%, #dadcd8 80%, #eef0ec 100%); }
  .photo--sea { left: 300px; top: 338px; width: 356px; height: 90px;
    background: linear-gradient(180deg, rgba(190,215,205,0) 0%, rgba(190,215,205,.55) 45%, rgba(226,222,206,.6) 100%); }
  .photo--seated { left: 468px; top: 228px; width: 62px; height: 220px; border-radius: 30px 30px 12px 12px;
    background: linear-gradient(180deg, #e9d8cc 0%, #c9b3a4 30%, #9a9a9a 60%, #3a3a3a 85%, #4a4a4a 100%); }
  .photo--headstand { left: 296px; top: 386px; width: 58px; height: 104px; border-radius: 24px;
    background: linear-gradient(200deg, #c7d3da 0%, #aebdc5 40%, #e6e6e6 70%, #d7dcd3 100%); }
  .photo--standing { left: 576px; top: 286px; width: 80px; height: 221px; border-radius: 36px 36px 0 0;
    background: linear-gradient(180deg, #e3c6b4 0%, #b59b8b 25%, #8a8a8a 40%, #1f1f1f 60%, #2a2a2a 100%); }
  .photo--portrait { left: 366px; top: 148px; width: 65px; height: 109px; border-radius: 8px; border: 1px solid #333;
    background: linear-gradient(180deg, #f2f2f2 0%, #cfcfcf 45%, #5c5c5c 75%, #2f2f2f 100%); }

  .logo-box { position: absolute; border: 1px solid #c9c9c9; display: flex; flex-direction: column; align-items: center; justify-content: center; gap: 8px; }
  .logo-box__dot { width: 22px; height: 22px; border-radius: 50%; background: var(--forest); }
  .logo-box__name { font-family: "Poppins", sans-serif; font-weight: 300; color: var(--logo-grey); text-align: center; line-height: 1.2; text-transform: uppercase; }

  /* outside spread */
  .intro { left: 185px; top: 62px; width: 108px; }
  .intro__title { font-weight: 700; font-size: 13px; line-height: 14.5px; color: var(--heading); }
  .intro__lead { margin-top: 9px; font-weight: 700; font-size: 7.4px; line-height: 8.9px; color: var(--heading); }
  .intro__body { font-size: 7.4px; line-height: 8.9px; color: var(--ink); }

  .logo-box--back { left: 113px; top: 244px; width: 106px; height: 106px; }
  .logo-box--back .logo-box__name { font-size: 10.5px; }

  .contact-panel { left: 52px; top: 375px; width: 227px; height: 132px; background: var(--forest); border-radius: 64px 64px 0 0; color: var(--white); text-align: center; }
  .contact-panel__icon { display: block; margin: 0 auto; }
  .contact-panel__phone { font-weight: 700; font-size: 16px; line-height: 18px; margin-top: 3px; letter-spacing: .3px; }
  .contact-panel__web { font-size: 10.5px; margin-top: 3px; }
  .contact-panel__web b, .web b { font-weight: 700; }

  .cover-panel { left: 366px; top: 0; width: 253px; height: 280px; background: var(--forest); border-radius: 0 0 64px 64px; }
  .cover-tab { left: 408px; top: 0; width: 170px; height: 128px; background: #fbfcfa; border-radius: 0 0 32px 32px; }
  .logo-box--cover { left: 445px; top: 19px; width: 96px; height: 95px; }
  .logo-box--cover .logo-box__name { font-size: 9.5px; }
  .cover-title { left: 366px; top: 140px; width: 253px; text-align: center; font-family: "Marcellus", serif; font-weight: 400; font-size: 29px; line-height: 28px; color: var(--white); }
  .cover-title__accent { color: var(--leaf); }
  .cover-place { left: 397px; top: 362px; font-size: 12.5px; line-height: 14px; color: var(--forest-deep); }
  .cover-place b, .cover-date b { font-weight: 700; }
  .cover-date { left: 541px; top: 362px; font-size: 11px; line-height: 13px; color: var(--forest-deep); }
  .cover-date b { font-size: 15px; }
  .web { font-size: 10.5px; color: var(--ink); }
  .web--cover { left: 366px; top: 479px; width: 253px; text-align: center; }

  /* inside spread */
  .quote-panel { left: 12px; top: 0; width: 304px; height: 101px; background: var(--forest); border-radius: 0 0 42px 42px; }
  .quote-panel__text { position: absolute; left: 50px; top: 36px; width: 200px; font-family: "Playfair Display", serif; font-weight: 600; font-size: 14px; line-height: 15px; color: var(--white); }
  .quote-panel__mark { position: absolute; font-family: "Playfair Display", serif; font-weight: 600; font-size: 30px; line-height: 1; color: var(--leaf); }

  .section-title { font-weight: 600; color: var(--heading); }
  .why { left: 38px; top: 112px; width: 253px; }
  .why .section-title { font-size: 13px; font-weight: 500; letter-spacing: .3px; margin-left: 2px; margin-bottom: 3px; }
  .copy { font-size: 6.2px; line-height: 7.9px; color: var(--ink); text-align: justify; }
  .copy p + p { margin-top: 7.5px; }
  .copy b { font-weight: 700; }
  .hold { left: 40px; top: 393px; width: 186px; }
  .hold .section-title { font-size: 12.5px; margin-bottom: 3px; }
  .hold .copy { text-align: left; }

  .approach { left: 366px; top: 30px; width: 255px; }
  .approach .section-title { font-size: 12.5px; margin-bottom: 3px; }
  .about { left: 443px; top: 146px; width: 180px; }
  .about .section-title { font-size: 12.5px; margin-bottom: 2px; }
  .about__copy { font-size: 5.4px; line-height: 6.9px; color: var(--ink); }
  .about__copy b { font-weight: 700; }

  .pathways-panel { left: 352px; top: 281px; width: 249px; height: 226px; background: var(--forest); border-radius: 40px 40px 0 0; }
  .pathways-panel__title { position: absolute; left: 20px; top: 17px; font-weight: 600; font-size: 12px; color: var(--white); }
  .pathway { position: absolute; width: 60px; margin-left: -30px; text-align: center; color: var(--white); font-weight: 500; font-size: 6.6px; line-height: 8.8px; }
  .pathway__icon { display: block; margin: 0 auto 4px; width: 24px; height: 24px; }
</style>
</head>
<body>

<section class="spread spread--outside" aria-label="Brochure outside spread">
  <div class="photo photo--kneeling" role="img" aria-label="Photo of a woman in a kneeling back-bend yoga pose on a deck by the sea"></div>
  <div class="photo photo--sea" role="img" aria-label="Soft misty seashore background"></div>

  <div class="abs intro">
    <h2 class="intro__title">Pathways We<br>Will Explore</h2>
    <p class="intro__lead">As these pathways weave together, a deeper journey unfolds—</p>
    <p class="intro__body">a movement from the surface of daily life into the quiet, spacious layers of the inner world.</p>
  </div>

  <div class="logo-box logo-box--back">
    <span class="logo-box__dot"></span>
    <span class="logo-box__name">The Velmira<br>Circle</span>
  </div>

  <div class="abs contact-panel">
    <svg class="contact-panel__icon" style="margin-top:22px" width="12" height="12" viewBox="0 0 24 24" aria-hidden="true">
      <path d="M6.6 10.8a15.1 15.1 0 0 0 6.6 6.6l2.2-2.2a1 1 0 0 1 1-.25 11.4 11.4 0 0 0 3.6.57 1 1 0 0 1 1 1V20a1 1 0 0 1-1 1A17 17 0 0 1 3 4a1 1 0 0 1 1-1h3.5a1 1 0 0 1 1 1c0 1.25.2 2.45.57 3.57a1 1 0 0 1-.25 1z" fill="var(--leaf)"/>
    </svg>
    <p class="contact-panel__phone">555-0142-7788</p>
    <svg class="contact-panel__icon" style="margin-top:4px" width="12" height="12" viewBox="0 0 24 24" aria-hidden="true">
      <circle cx="12" cy="12" r="10" fill="none" stroke="var(--leaf)" stroke-width="2"/>
      <ellipse cx="12" cy="12" rx="4.5" ry="10" fill="none" stroke="var(--leaf)" stroke-width="2"/>
      <path d="M2 12h20" stroke="var(--leaf)" stroke-width="2"/>
    </svg>
    <p class="contact-panel__web">www.<b>velmira-circle</b>.com</p>
  </div>

  <div class="abs cover-panel"></div>
  <div class="abs cover-tab"></div>
  <div class="logo-box logo-box--cover">
    <span class="logo-box__dot"></span>
    <span class="logo-box__name">The Velmira<br>Circle</span>
  </div>
  <div class="photo photo--seated" role="img" aria-label="Photo of a woman meditating cross-legged with palms joined overhead"></div>
  <h1 class="abs cover-title"><span class="cover-title__accent">Pathways</span><br>to Our<br>True Essence</h1>

  <p class="abs cover-place"><b>TUSCANY,</b><br>ITALY</p>
  <p class="abs cover-date"><b>25–29</b><br>JUNE 2026</p>
  <p class="abs web web--cover">www.<b>velmira-circle</b>.com</p>
</section>

<section class="spread spread--inside" aria-label="Brochure inside spread">
  <div class="abs quote-panel">
    <span class="quote-panel__mark" style="left:24px;top:34px">“</span>
    <p class="quote-panel__text">Within the quiet of your being, your essence waits to be remembered.</p>
    <span class="quote-panel__mark" style="left:231px;top:58px">”</span>
  </div>

  <div class="photo photo--headstand" role="img" aria-label="Photo of a woman in a supported headstand variation"></div>

  <div class="abs why">
    <h2 class="section-title">WHY I CREATED THIS RETREAT</h2>
    <div class="copy">
      <p>My relationship with yoga began in 1997, while I was working with the Alder Global Forum in Rome. To be honest, I hated it at first. My body was stiff, tense, and unfamiliar to me. The practice felt uncomfortable—an almost psycho-physical irritation I couldn’t quite explain. And yet, something was shifting. A colleague commented, <b>“You’re so much nicer when you come back from yoga,”</b> and I began to notice moments of awareness I had never experienced before—my toes, the palms of my hands, a single muscle along my back. Something inside me was waking up. Years later, as I transitioned out of an intense, travel-heavy career and trained for the Harborline Marathon, yoga resurfaced—not as stretching, but as stillness.</p>
      <p>Though I still couldn’t touch my toes, I realised that an hour on the mat quieted my mind more deeply than 26.2 miles of running ever could. The penny dropped. Yoga wasn’t simply physical; it was one doorway inward. They say, <b>“You will find yourself on your mat,”</b> and that was becoming true. I stepped into my first teacher training, not to teach, but to understand. It felt less like entering a new world and more like returning to an original one. Fast-forward through years of practice, curiosity, study, and exploration, and I have come to understand something essential: there is no single path. Dogma has no place in self-discovery. Each of us is unique, and each of us will resonate with different tools at different moments in our lives.</p>
      <p>What supports us today may shift tomorrow. This is not only natural—it is to be honoured. This retreat is rooted in that philosophy. It is not a yoga retreat, though yoga is one of the practices we draw from. Instead, it is a discerning, intelligent, and elegant container for gentle yet deep inner work. My intention is to offer a constellation of modalities—movement, breath, meditation, somatics, energy practices, craftwork, nature immersion—so you may discover what truly serves you. The group remains intentionally small so that each person receives the attention, guidance, and individualisation they need. This is an invitation to step toward your essence, in your own way, at your own rhythm.</p>
    </div>
  </div>

  <div class="abs hold">
    <h2 class="section-title">How I Hold Space</h2>
    <p class="copy">I have cultivated a quiet, practiced intuition that allows me to meet people exactly where they are. Through energy work, meditation, and somatics, I’ve learned to sense subtle shifts within a room or within an individual. This attunement shows me when to guide, when to soften, and when to simply allow — and when needed, when to be clear and firm. I am able to hold people gently yet accountably, ensuring they do not slip away from the very work they came to meet.</p>
  </div>

  <div class="abs approach">
    <h2 class="section-title">The Essence Approach</h2>
    <p class="copy">My approach is grounded in the understanding that self-discovery is not linear and not prescriptive. We each arrive with different histories, patterns, and sensitivities, and therefore no single modality can speak to everyone in the same way. I work by offering a curated selection of practices—movement, breath, somatics, meditation, energetic work, and creative exploration—so you can experience what truly resonates for you. I invite each person to explore with curiosity rather than expectation, allowing space for insight, release, or stillness to arise naturally. My intention is to guide with clarity while honouring your autonomy and inner wisdom.</p>
  </div>

  <div class="photo photo--portrait" role="img" aria-label="Black and white portrait of the retreat host"></div>
  <div class="abs about">
    <h2 class="section-title">About Me</h2>
    <p class="about__copy"><b>I am an Ashtanga practitioner who teaches various styles of yoga—dynamic, hatha, yin, nidra—</b> with a somatic and intuitive approach. I teach meditation, breathwork, and energy practices, and I am an RYT-500hr teacher certified in advanced pranayama and meditation. I have been an LCF Certified Coach for <b>over 10 years.</b> My earlier career spanned international development with the Northbridge Commission, INGOs, the Alder Global Forum, and my own consultancy focused on creating inclusive organisations. These experiences shaped my ability to listen deeply, hold space, and support transformation with clarity and compassion.</p>
  </div>

  <div class="abs pathways-panel">
    <h2 class="pathways-panel__title">Pathways We Will Explore</h2>
    <svg width="0" height="0" style="position:absolute" aria-hidden="true">
      <defs>
        <g id="ring"><circle cx="12" cy="12" r="11.5" fill="var(--white)"/><circle cx="12" cy="12" r="9.5" fill="none" stroke="var(--forest)" stroke-width=".8"/></g>
      </defs>
    </svg>

    <div class="pathway" style="left:42px;top:55px">
      <svg class="pathway__icon" viewBox="0 0 24 24" aria-hidden="true"><use href="#ring"/><path d="M13 6.5l-4 6h3l-1 5 4-6h-3z" fill="none" stroke="var(--forest)" stroke-width=".9" stroke-linejoin="round"/></svg>
      Evolove<br>Your Energy
    </div>
    <div class="pathway" style="left:91px;top:55px">
      <svg class="pathway__icon" viewBox="0 0 24 24" aria-hidden="true"><use href="#ring"/><path d="M7 14c2 0 3 1 5 1s3-1 5-2M7 16.5h7M12 7c-2 1.5-2 4 0 5 2-1 2-3.5 0-5z" fill="none" stroke="var(--forest)" stroke-width=".9" stroke-linecap="round"/></svg>
      Immerse in<br>Frequency
    </div>
    <div class="pathway" style="left:139px;top:55px">
      <svg class="pathway__icon" viewBox="0 0 24 24" aria-hidden="true"><use href="#ring"/><path d="M9 17v-3a4 4 0 1 1 6-3.5M15 13v4M14 8.5h3M14.5 10.5h3" fill="none" stroke="var(--forest)" stroke-width=".9" stroke-linecap="round"/></svg>
      Harness<br>Your Breath
    </div>
    <div class="pathway" style="left:191px;top:55px">
      <svg class="pathway__icon" viewBox="0 0 24 24" aria-hidden="true"><use href="#ring"/><circle cx="12" cy="10" r="2" fill="none" stroke="var(--forest)" stroke-width=".9"/><path d="M8.5 16a3.5 3.5 0 0 1 7 0z" fill="none" stroke="var(--forest)" stroke-width=".9"/><circle cx="12" cy="12" r="6.5" fill="none" stroke="var(--forest)" stroke-width=".7"/></svg>
      Embodied<br>Awakening
    </div>

    <div class="pathway" style="left:42px;top:117px">
      <svg class="pathway__icon" viewBox="0 0 24 24" aria-hidden="true"><use href="#ring"/><circle cx="13.5" cy="10.5" r="3.5" fill="none" stroke="var(--forest)" stroke-width=".9"/><path d="M11 13l-4 4" stroke="var(--forest)" stroke-width="1.3" stroke-linecap="round"/></svg>
      Shadow<br>Exploration
    </div>
    <div class="pathway" style="left:91px;top:117px">
      <svg class="pathway__icon" viewBox="0 0 24 24" aria-hidden="true"><use href="#ring"/><circle cx="12" cy="12" r="1.4" fill="var(--forest)"/><path d="M9.5 9.5a3.5 3.5 0 0 0 0 5M14.5 9.5a3.5 3.5 0 0 1 0 5M8 8a5.6 5.6 0 0 0 0 8M16 8a5.6 5.6 0 0 1 0 8" fill="none" stroke="var(--forest)" stroke-width=".9" stroke-linecap="round"/></svg>
      Reiki<br>Healing
    </div>
    <div class="pathway" style="left:139px;top:117px">
      <svg class="pathway__icon" viewBox="0 0 24 24" aria-hidden="true"><use href="#ring"/><path d="M12 6l-3 5h2l-2.5 4h7L13 11h2z" fill="none" stroke="var(--forest)" stroke-width=".9" stroke-linejoin="round"/><path d="M12 15v2.5M7 17.5h10" stroke="var(--forest)" stroke-width=".9" stroke-linecap="round"/></svg>
      Forest<br>Bathing
    </div>
    <div class="pathway" style="left:191px;top:117px">
      <svg class="pathway__icon" viewBox="0 0 24 24" aria-hidden="true"><use href="#ring"/><path d="M10.5 16.5l-2-3a1 1 0 0 1 1.6-1.1l.9 1V8a1 1 0 0 1 2 0v3.5l2.6.5a1.5 1.5 0 0 1 1.2 1.7l-.5 2.8" fill="none" stroke="var(--forest)" stroke-width=".9" stroke-linecap="round" stroke-linejoin="round"/></svg>
      Centering at<br>Your<br>Fingertips
    </div>
  </div>

  <div class="photo photo--standing" role="img" aria-label="Photo of a woman standing in tree pose with palms joined"></div>
</section>

</body>
</html>
```